Deaths in the gang

Creation of a cover for the book "Un soir de pluie" (Title to be used, not the English one)
Size: 14 x 20.5 cm (vertical; with bleed-off on the top, the right side and the bottom)
Title: “One rainy evening” (this title has no meaning, it's just an expression)
Author: "Mathieu Dervanche"
Publisher: “Editions Pavane” (at the bottom of the page).
Key Words:
gangster, escape, hold up, murders, jewels, love, young woman with auburn hair.
Story:
Julien Marbot, a very dangerous gangster and unscrupulous murderer, escapes from prison in order to organize a new hold up. Lieutenant Vidal, one of the police officers in charge of the investigation falls in love with Sandrine Moulet, a lovely prison supervisor who has been held hostage during the escape of Marbot.
But Vidal realizes that Sandrine doesn't tell him all the truth.
And soon, several members of the gang die in mysterious circumstances…
The unbelievable truth will be revealed tardily.
Target Market(s)
Readers of detective stories
Industry/Entity Type
Book
Look and feel

```html
<!DOCTYPE html>
<html lang="fr">
<head>
<meta charset="utf-8">
<title>Un soir de pluie — Mathieu Dervanche</title>
<link rel="stylesheet" href="https://fonts.googleapis.com/css2?family=Jost:wght@300;400&family=League+Spartan:wght@700&display=swap">
<style>
  :root {
    --backdrop: #232f3d;
    --cover-ink: #0f171e;
    --cover-deep: #0a1015;
    --corridor-light: #cfe3ec;
    --corridor-haze: #6f93a6;
    --wall-steel: #3d5a6b;
    --wall-shadow: #16242d;
    --title-red: #ee1549;
    --paper-white: #f1f3f4;
  }
  * { margin: 0; padding: 0; box-sizing: border-box; }
  html, body {
    width: 1200px;
    height: 926px;
    overflow: hidden;
    background: var(--backdrop);
  }
  .stage {
    position: relative;
    width: 1200px;
    height: 926px;
  }
  .book-cover {
    position: absolute;
    left: 340px;
    top: 48px;
    width: 519px;
    height: 830px;
    background: var(--cover-ink);
    overflow: hidden;
  }
  .cover-scene {
    position: absolute;
    left: 0;
    top: 200px;
    width: 100%;
    height: 630px;
    background:
      /* ceiling lamp at the far end of the corridor */
      radial-gradient(ellipse 12% 8% at 50% 23%, rgba(240, 250, 255, 0.95) 0%, rgba(207, 227, 236, 0.6) 45%, transparent 100%),
      /* misty light filling the corridor */
      radial-gradient(ellipse 30% 42% at 52% 36%, rgba(150, 190, 208, 0.7) 0%, rgba(111, 147, 166, 0.38) 45%, transparent 100%),
      /* wet floor reflection */
      radial-gradient(ellipse 22% 26% at 54% 78%, rgba(111, 147, 166, 0.3) 0%, transparent 100%),
      /* left cell wall, lit high and fading toward the floor */
      radial-gradient(ellipse 22% 40% at 10% 32%, rgba(110, 150, 172, 0.55) 0%, rgba(61, 90, 107, 0.3) 50%, transparent 100%),
      /* right cell wall */
      radial-gradient(ellipse 22% 42% at 92% 26%, rgba(130, 170, 190, 0.6) 0%, rgba(61, 90, 107, 0.3) 50%, transparent 100%),
      /* wall-to-corridor tonal bands */
      linear-gradient(90deg,
        var(--wall-shadow) 0%, var(--wall-steel) 9%, #1d303c 20%, #2b4656 30%,
        var(--cover-deep) 38%, #1b2e39 50%, var(--cover-deep) 64%,
        #2b4656 72%, #1d303c 81%, var(--wall-steel) 91%, var(--wall-shadow) 100%),
      var(--cover-deep);
    -webkit-mask-image: linear-gradient(180deg, transparent 0%, #000 18%, #000 68%, rgba(0,0,0,0.3) 100%);
            mask-image: linear-gradient(180deg, transparent 0%, #000 18%, #000 68%, rgba(0,0,0,0.3) 100%);
  }
  .author-name {
    position: absolute;
    top: 30px;
    left: 0;
    width: 100%;
    text-align: center;
    font-family: "Jost", sans-serif;
    font-weight: 400;
    font-size: 24px;
    letter-spacing: 0.45em;
    padding-left: 0.45em;
    color: var(--paper-white);
  }
  .book-title {
    position: absolute;
    left: 0;
    top: 86px;
    width: 100%;
    text-align: center;
    font-family: "League Spartan", sans-serif;
    font-weight: 700;
    color: var(--title-red);
    line-height: 1;
  }
  .book-title span { display: block; }
  .title-line-1 { font-size: 106px; height: 78px; letter-spacing: -0.01em; }
  .title-line-2 { font-size: 68px;  height: 54px; }
  .title-line-3 { font-size: 90px;  height: 74px; letter-spacing: -0.01em; }
  .title-line-4 { font-size: 70px;  height: 52px; }
  .publisher {
    position: absolute;
    top: 758px;
    left: 0;
    width: 100%;
    text-align: center;
    font-family: "Jost", sans-serif;
    font-weight: 300;
    font-size: 25px;
    color: var(--paper-white);
  }
</style>
</head>
<body>
  <main class="stage">
    <article class="book-cover">
      <div class="cover-scene" role="img" aria-label="Illustration: a man and a young woman with auburn hair in long coats standing close in a dim, rain-wet prison corridor lined with barred cells, lit by a single lamp, a lone figure waiting in the mist behind them"></div>

      <p class="author-name">MATHIEU DERVANCHE</p>

      <h1 class="book-title" aria-label="Un soir de pluie">
        <span class="title-line-1">UN</span>
        <span class="title-line-2">SOIR</span>
        <span class="title-line-3">DE</span>
        <span class="title-line-4">PLUIE</span>
      </h1>

      <p class="publisher">Editions Pavane</p>
    </article>
  </main>
</body>
</html>
```